Specialised investor in e-mobility and energy wants business card design

We need a business card design that fits our existing corporate design. <The look and feel must be 'sharp'/'clean', dynamic, communicate momentum, professionalism etc (as one would imagine from a firm in the financial sector). We like the idea of a reverse-side of the card that includes the logo, and the name and contact details on the other. We expect the deliverable to be whatever format might be required to be able to get cards printed directly by a service such as tandor press. Our website is www.orm.capital

```html
<!DOCTYPE html>
<html lang="en">
<head>
<meta charset="utf-8">
<title>ORM Capital – Business Card</title>
<link rel="stylesheet" href="https://fonts.googleapis.com/css2?family=Questrial&family=Montserrat:wght@700&display=swap">
<style>
  :root {
    --bg: #e4e4e3;
    --paper: #f5f5f6;
    --forest: #2d4821;
    --leaf: #80ac47;
    --ink-light: #eef1ea;
    --emboss: #3b5c2c;
  }
  * { box-sizing: border-box; margin: 0; padding: 0; }
  html, body { width: 1200px; height: 1200px; overflow: hidden; }
  body {
    background: var(--bg);
    font-family: "Questrial", "Century Gothic", sans-serif;
    position: relative;
  }
  .card {
    position: absolute;
    left: 257px;
    width: 686px;
    height: 392px;
    border-radius: 20px;
    overflow: hidden;
  }
  .card--front { top: 165px; background: var(--paper); }
  .card--back { top: 653px; background: var(--forest); }

  .card__swoosh { position: absolute; inset: 0; width: 100%; height: 100%; }

  .brand {
    position: absolute;
    font-family: "Questrial", "Century Gothic", sans-serif;
    font-weight: 400;
    white-space: nowrap;
    line-height: 1;
  }
  .card--front .brand {
    left: 30px; top: 54px;
    font-size: 52px;
    color: var(--forest);
  }
  .card--back .brand {
    left: 0; right: 0; top: 166px;
    text-align: center;
    font-size: 62px;
    color: var(--emboss);
  }

  .contact {
    position: absolute;
    right: 49px;
    top: 203px;
    text-align: right;
    color: var(--ink-light);
  }
  .contact__name {
    font-family: "Montserrat", "Century Gothic", sans-serif;
    font-weight: 700;
    font-size: 22px;
    color: var(--leaf);
    letter-spacing: 0.3px;
    line-height: 26px;
  }
  .contact__role { font-size: 15px; line-height: 20px; }
  .contact__city { font-size: 16.5px; line-height: 20px; margin-top: 12px; }
  .contact__line {
    display: flex; justify-content: flex-end; align-items: center;
    gap: 12px; font-size: 16px; line-height: 22px;
  }
  .contact__line--phone { margin-top: 13px; }
  .contact__icon { width: 14px; height: 14px; fill: var(--leaf); }
  .contact__web {
    font-size: 16px; font-weight: 700;
    font-family: "Montserrat", sans-serif;
    color: var(--leaf);
    margin-top: 9px;
    letter-spacing: 0.2px;
  }
</style>
</head>
<body>
  <section class="card card--front">
    <svg class="card__swoosh" viewBox="0 0 800 457" preserveAspectRatio="none" aria-hidden="true">
      <path d="M0,382 C210,250 460,152 650,150 C725,150 770,168 800,188 L800,457 L0,457 Z" fill="var(--leaf)"/>
      <path d="M0,446 C220,292 500,172 680,170 C742,170 780,185 800,198 L800,457 L0,457 Z" fill="var(--forest)" stroke="#ffffff" stroke-width="2"/>
    </svg>

    <div class="brand">ORM Capital</div>

    <div class="contact">
      <div class="contact__name">MARCUS ELLERY</div>
      <div class="contact__role">Managing Director</div>
      <div class="contact__city">Westvale, Northland</div>
      <div class="contact__line contact__line--phone">
        <span>+41 79555 0148</span>
        <svg class="contact__icon" viewBox="0 0 24 24" aria-hidden="true"><path d="M6.6 10.8a15.1 15.1 0 0 0 6.6 6.6l2.2-2.2c.3-.3.7-.4 1-.2 1.1.4 2.3.6 3.6.6.6 0 1 .4 1 1V20c0 .6-.4 1-1 1A17 17 0 0 1 3 4c0-.6.4-1 1-1h3.5c.6 0 1 .4 1 1 0 1.3.2 2.5.6 3.6.1.3 0 .7-.2 1z"/></svg>
      </div>
      <div class="contact__line">
        <span>marcus@orm.capital</span>
        <svg class="contact__icon" viewBox="0 0 24 24" aria-hidden="true"><path d="M2 5h20v14H2z M3.5 6.5 12 12.5l8.5-6z" fill-rule="evenodd"/></svg>
      </div>
      <div class="contact__web">www.orm.capital</div>
    </div>
  </section>

  <section class="card card--back">
    <div class="brand">ORM Capital</div>
  </section>
</body>
</html>
```